Tire trade

Hello, I would like to make A5 flyers for my garage, with the 'bramel tires' logo.
Registration: Sale and fitting of tires of all brands (also ordered by you) Guarding of your tires

Target Market(s)

All motorists in my area

Industry/Entity Type

Vente de pneus

Font styles to use
Serif

Colors
EE7325
F08F49
F5BC92
FAE3D3
FDF4ED

Requirements
Must have
• My logo, the place (Val-d'Illiez)
Nice to have
• Simple and eye-catching
Should not have
• pink

```html
<!DOCTYPE html>
<html lang="en">
<head>
<meta charset="utf-8">
<title>Bramel Tires – Flyer</title>
<link href="https://fonts.googleapis.com/css2?family=Zilla+Slab:ital,wght@0,700;1,700&display=swap" rel="stylesheet">
<style>
  :root {
    --orange: #ee7325;
    --orange-mid: #f08f49;
    --orange-soft: #f5bc92;
    --peach: #fae3d3;
    --cream: #fdf4ed;
    --grey: #5f6064;
    --grey-dark: #2e2f33;
    --white: #ffffff;
    --stage: #efefef;
  }
  * { margin: 0; padding: 0; box-sizing: border-box; }
  html, body {
    width: 925px; height: 1200px; overflow: hidden;
    background: var(--stage);
  }
  .flyer {
    position: absolute; left: 38px; top: 0;
    width: 849px; height: 1200px;
    background: var(--white);
    overflow: hidden;
    font-family: "Zilla Slab", Georgia, serif;
  }
  .flyer__shapes { position: absolute; inset: 0; }
  .brand {
    position: absolute; left: 56px; top: 96px;
    display: flex; align-items: center; gap: 20px;
  }
  .brand__dot {
    width: 44px; height: 44px; border-radius: 50%;
    background: var(--orange);
  }
  .brand__name {
    font-weight: 700; font-size: 112px; line-height: 1;
    color: var(--grey-dark); text-transform: lowercase;
  }
  .phone {
    position: absolute; left: 178px; top: 252px;
    font-style: italic; font-weight: 700; font-size: 68px; line-height: 1;
    color: var(--orange);
  }
  .location {
    position: absolute; left: 182px; top: 332px;
    font-weight: 700; font-size: 32px; line-height: 1;
    color: var(--grey); letter-spacing: 1px;
  }
  .headline {
    position: absolute; left: 162px; top: 654px;
    font-style: italic; font-weight: 700; text-transform: uppercase;
    line-height: 0.84;
  }
  .headline__line { display: block; }
  .headline__accent { color: var(--orange); }
  .headline__main { color: var(--grey); }
  .headline__line--one { font-size: 92px; }
  .headline__line--two { font-size: 76px; }
  .headline__line--three { font-size: 112px; margin-left: 70px; }
  .services {
    position: absolute; left: 232px; top: 878px; width: 300px;
    font-style: italic; font-weight: 700; text-transform: uppercase;
    font-size: 26px; line-height: 1.1; color: var(--grey);
  }
  .services__note { font-weight: 700; font-size: 24px; opacity: 0.85; }
</style>
</head>
<body>
  <main class="flyer">
    <svg class="flyer__shapes" width="849" height="1200" viewBox="0 0 849 1200">
      <defs>
        <linearGradient id="trackGrad" x1="0" y1="0" x2="0" y2="1">
          <stop offset="0" stop-color="#f5bc92"/>
          <stop offset="1" stop-color="#ee7325"/>
        </linearGradient>
        <linearGradient id="workshopGrad" x1="0" y1="0" x2="1" y2="1">
          <stop offset="0" stop-color="#c9cbd0"/>
          <stop offset="1" stop-color="#4a4c52"/>
        </linearGradient>
      </defs>
      <path class="tire-track" role="img" aria-label="Orange tire track curving down and across the page"
            d="M660 0 L790 0 C820 120 849 200 849 260 L849 490
               C760 555 600 600 380 622
               C460 590 565 555 640 515
               C720 465 760 400 740 330
               C700 220 660 120 660 0 Z"
            fill="url(#trackGrad)" opacity="0.85"/>
      <polygon class="photo photo--workshop" role="img" aria-label="Photo of a mechanic inflating a tire"
               points="0,1200 0,808 140,808 198,945 150,945 185,1200" fill="url(#workshopGrad)"/>
      <polygon class="photo photo--fitting" role="img" aria-label="Photo of a mechanic carrying a tire in the garage"
               points="849,640 849,1070 700,1070 708,1030 540,1030 660,660" fill="url(#workshopGrad)"/>
    </svg>

    <div class="brand">
      <span class="brand__dot"></span>
      <span class="brand__name">bramel tires</span>
    </div>

    <p class="phone">079/555.01.23</p>
    <p class="location">Val-d'Illiez</p>

    <h1 class="headline">
      <span class="headline__line headline__line--one headline__accent">Guarding</span>
      <span class="headline__line headline__line--two"><span class="headline__accent">of</span><span class="headline__main">your</span></span>
      <span class="headline__line headline__line--three headline__main">Tires</span>
    </h1>

    <p class="services">Sale and fitting of tires of all brands <span class="services__note">(also ordered by you)</span></p>
  </main>
</body>
</html>
```